Strong, modern, clean Business Card design

Looking for a stunning, but CLEAN business card design. While we are a faith-based organization, we do NOT want this to look religious.

Industry/Entity Type

Non-Profit

Contact Information for Business Card

Dale Munroe | Lead Pastor
dale@BrightHarvestHope.org
970-555-0148
PO Box 7316
Fernhollow, MT 80571

Font styles to use
Serif
Sans Serif

Requirements
Should not have
• Religious imagery or symbolism

```html
<!DOCTYPE html>
<html lang="en">
<head>
<meta charset="utf-8">
<title>Brightwater Church – Business Card</title>
<link rel="stylesheet" href="https://fonts.googleapis.com/css2?family=Libre+Caslon+Text:wght@400;700&display=swap">
<style>
  :root {
    --paper: #ffffff;
    --card: #d7c2bf;
    --ink: #4e7890;
  }
  * { margin: 0; padding: 0; box-sizing: border-box; }
  html, body {
    width: 1002px; height: 1200px; overflow: hidden;
    background: var(--paper);
  }
  body {
    position: relative;
    font-family: "Libre Caslon Text", Georgia, serif;
    color: var(--ink);
  }
  .card {
    position: absolute;
    background: var(--card);
  }
  .card--front { left: 121px; top: 69px; width: 563px; height: 322px; }
  .card--back  { left: 121px; top: 440px; width: 585px; height: 669px; }

  .contact-list {
    position: absolute; left: 36px; top: 52px;
    list-style: none;
    font-size: 30px; line-height: 46px;
    white-space: nowrap;
  }
  .wordmark {
    position: absolute;
    font-size: 22px; line-height: 1;
    white-space: nowrap;
  }
  .card--front .wordmark { right: 26px; top: 256px; }
  .card--back .wordmark { right: 28px; top: 600px; }

  .church-name {
    position: absolute; left: 42px; top: 40px; width: 495px;
    font-size: 31px; font-weight: 700; line-height: 1;
    letter-spacing: 0.07em;
    text-align: center; white-space: nowrap;
  }
  .rule {
    position: absolute; left: 42px; width: 495px; height: 1px;
    background: var(--ink);
  }
  .rule--top { top: 76px; }
  .rule--bottom { top: 542px; }

  .mailing-address {
    position: absolute; left: 505px; top: 206px;
    writing-mode: vertical-rl;
    font-style: normal;
    font-size: 19px; line-height: 29px;
    white-space: nowrap;
  }
  .signature {
    position: absolute; left: 41px; top: 566px;
    font-size: 20px; line-height: 33px;
    white-space: nowrap;
  }
</style>
</head>
<body>
  <section class="card card--front">
    <ul class="contact-list">
      <li>Dale Munroe | Lead Pastor</li>
      <li>dale@BrightHarvestHope.org</li>
      <li>970-555-0148</li>
      <li>PO Box 7316</li>
      <li>Fernhollow, MT 80571</li>
    </ul>
    <div class="wordmark">Brightwater</div>
  </section>

  <section class="card card--back">
    <h1 class="church-name">BRIGHTWATER CHURCH</h1>
    <div class="rule rule--top"></div>
    <address class="mailing-address">
      <span>PO Box 7316</span><br>
      <span>Fernhollow, MT 80571</span>
    </address>
    <div class="rule rule--bottom"></div>
    <div class="signature">
      <p>Dale Munroe | Lead Pastor</p>
      <p>dale@BrightHarvestHope.org</p>
    </div>
    <div class="wordmark">Brightwater</div>
  </section>
</body>
</html>
```